The title of the book is: Resonant Foundations for Builders
I need a front and back cover for my new book.
This is a reference book written to teach architects the basics of acoustics and sound.
The subtitle is: The handbook on echoes and tone most designers hoped their teachers had given them
Author is: Dorian Wick
Publisher: PLOV Press
Primary colors desired are deep red, and deep rich gold. A splash of cobalt blue might be nice too.
Black and/or White fonts
I'm a fan of art deco designs, but I'm also a minimalist, so I'd like something that's not too busy.
This will be used for both a paperback and ebook. Format for "portrait" viewing.
Final files need to be high-res .jpg. Size: 1873 pixels on the longest side, 1600 pixels on the shortest side (350 dpi)
The inside cover page is attached as a reference only.

Target Market(s)

Architects

Industry/Entity Type

Architecture, interior design, and pro audio

Font styles to use
Sans Serif
Other font styles liked:
• Arial

Colors
0054AA
0677BA
7BADD7
CADEEF
E8F1F8
FFC000
F8CF3A
FAE287
FDF2CF
FEFAEE
EB3D1F
EC4F4E
F09395
F8D3D4
FCEDEE

Requirements
Must have
• Elegant font cover design
Nice to have
• Spine and back cover design to compliment front cover. Spine will be roughly 1/2"
Should not have
• Anything that will date the book based on front cover graphics

```html
<!DOCTYPE html>
<html lang="en">
<head>
<meta charset="utf-8">
<title>Resonant Foundations for Builders — Covers</title>
<link rel="stylesheet" href="https://fonts.googleapis.com/css2?family=Oswald:wght@600;700&family=Montserrat:wght@400;600;700&display=swap">
<style>
  :root {
    --stage: #43596a;
    --cover-red: #6b2727;
    --cover-red-deep: #5a1f20;
    --title-red: #7c2a2b;
    --gold: #c98b3c;
    --gold-light: #f0c27a;
    --frame-white: #ffffff;
    --teal-light: #2fa89c;
    --teal-dark: #0b3a37;
    --ink-white: #ffffff;
    --ink-soft: #d9c4c2;
    --rule: rgba(255,255,255,0.45);
  }
  * { margin: 0; padding: 0; box-sizing: border-box; }
  html, body {
    width: 1200px; height: 955px; overflow: hidden;
    background: var(--stage);
    font-family: "Montserrat", Arial, sans-serif;
  }
  .stage { position: relative; width: 1200px; height: 955px; }
  .cover {
    position: absolute; top: 190px;
    width: 535px; height: 565px;
    background: var(--cover-red);
    box-shadow: 0 14px 30px rgba(0,0,0,0.35);
    overflow: hidden;
  }
  .cover--front { left: 50px; }
  .cover--back { left: 615px; }
  .cover__texture {
    position: absolute; inset: 0;
    background: radial-gradient(circle at 75% 20%, #743030 0%, var(--cover-red) 45%, var(--cover-red-deep) 100%);
  }

  /* Front */
  .hero-frame {
    position: absolute; left: -20px; top: 58px;
    width: 290px; height: 420px;
    border-radius: 0 34px 34px 0;
    background: linear-gradient(160deg, var(--gold-light), var(--gold) 50%, #8a5a22);
    padding: 5px 5px 5px 25px;
  }
  .hero-frame__inner {
    width: 100%; height: 100%;
    border-radius: 0 30px 30px 0;
    background: var(--frame-white);
    padding: 10px 10px 10px 0;
  }
  .hero-photo {
    width: 100%; height: 100%;
    border-radius: 0 22px 22px 0;
    background: radial-gradient(ellipse at 30% 35%, var(--teal-light) 0%, #1b6e67 45%, var(--teal-dark) 100%);
  }
  .title-block {
    position: absolute; left: 270px; top: 82px;
    width: 240px; height: 390px;
    background: var(--title-red);
    box-shadow: -4px 6px 14px rgba(0,0,0,0.35);
    display: flex; flex-direction: column; justify-content: center;
    padding: 0 12px;
    font-family: "Oswald", "Arial Narrow", sans-serif;
    font-weight: 700; color: var(--ink-white);
    text-transform: uppercase; line-height: 1;
    text-shadow: 2px 3px 4px rgba(0,0,0,0.45);
    text-align: left;
    white-space: nowrap;
  }
  .title-block__line--a { font-size: 51px; }
  .title-block__line--b { font-size: 37px; }
  .title-block__line--c { font-size: 128px; line-height: 0.95; }
  .title-block__line--d { font-size: 52px; }

  .subtitle {
    position: absolute; left: 0; right: 0;
    text-align: center; color: var(--ink-soft);
    text-transform: uppercase;
  }
  .subtitle--front { top: 482px; left: 120px; right: 20px; font-size: 10px; line-height: 1.25; }
  .subtitle__lead { letter-spacing: 0.55em; }
  .subtitle__key { color: var(--ink-white); font-weight: 700; letter-spacing: 0.03em; }
  .subtitle__rest { letter-spacing: 0.06em; }

  .byline {
    position: absolute; text-align: center;
    color: var(--ink-soft); font-size: 10px;
    letter-spacing: 0.4em; text-transform: uppercase;
    padding: 3px 18px;
    border-bottom: 1px solid var(--rule);
    white-space: nowrap;
    transform: translateX(-50%);
  }
  .byline strong { color: var(--ink-white); font-weight: 700; }
  .byline--front { left: 317px; top: 534px; }

  /* Back */
  .back-title {
    position: absolute; left: 0; right: 0; top: 232px;
    text-align: center; color: var(--ink-white);
    font-weight: 700; font-size: 15px; line-height: 1.1;
    text-transform: uppercase;
  }
  .subtitle--back { top: 274px; font-size: 9.5px; line-height: 1.25; }
  .byline--back { left: 50%; top: 490px; }
  .publisher {
    position: absolute; left: 0; right: 0; top: 516px;
    text-align: center; color: var(--ink-white);
    font-size: 10px; font-weight: 600;
  }
</style>
</head>
<body>
<main class="stage">

  <section class="cover cover--front" aria-label="Front cover">
    <div class="cover__texture" role="img" aria-label="Faint gold blueprint linework of concentric arcs and floor plans on deep red"></div>
    <div class="hero-frame">
      <div class="hero-frame__inner">
        <div class="hero-photo" role="img" aria-label="Close-up photograph of a teal diamond-patterned acoustic wall panel"></div>
      </div>
    </div>
    <h1 class="title-block">
      <span class="title-block__line--a">Resonant</span>
      <span class="title-block__line--b">Foundations</span>
      <span class="title-block__line--c">For</span>
      <span class="title-block__line--d">Builders</span>
    </h1>
    <p class="subtitle subtitle--front">
      <span class="subtitle__lead">The handbook on</span><br>
      <span class="subtitle__key">Echoes and tone</span><br>
      <span class="subtitle__rest">Most designers hoped their</span><br>
      <span class="subtitle__rest">teachers had given them</span>
    </p>
    <p class="byline byline--front">By <strong>Dorian Wick</strong></p>
  </section>

  <section class="cover cover--back" aria-label="Back cover">
    <div class="cover__texture" role="img" aria-label="Faint gold blueprint linework of circular plans and grid markers on deep red"></div>
    <h2 class="back-title">Resonant Foundations<br>for Builders</h2>
    <p class="subtitle subtitle--back">
      <span class="subtitle__lead">The handbook on</span><br>
      <span class="subtitle__key">Echoes and tone</span><br>
      <span class="subtitle__rest">Most designers hoped their</span><br>
      <span class="subtitle__rest">teachers had given them</span>
    </p>
    <p class="byline byline--back">By <strong>Dorian Wick</strong></p>
    <p class="publisher">Publisher: PLOV Press</p>
  </section>

</main>
</body>
</html>
```